Education provider needs a landing page for its brand

We need a landing page for an advertising campaign that we are currently running on jobtrawl.com.au.
We're Fernbrook Institute. We offer Australian online qualifications (courses) that help people get jobs with the right knowledge.
We'd like a landing page that shows our quirky, fun style that breaks away from traditional, conservative education advertising. The final landing page needs to be a strong converter for leads as it can take up to 90 days for someone to decide to study a course.
Check out our website. www.fernbrook.edu.au

We also like the attached landing pages by Zolt and Pellow Academy.

Target Market(s)

25-45 yr olds who have recently searched for a course to study on Trawl.

Font styles to use
Sans Serif

Colors
3276b5
85acd3
ecf5f6
87d0c7

Requirements
Must have
• - Simple and uncluttered
- Logo
- Video - https://vidhost.example/qT7mWx2LcaB
- 3 x dot points about why Fernbrook is your best educator partner
- It needs a lead form to capture user's details so we can nurture them in an email campaign. This will be a 'Learn More' button that allows them to add their name and email address and they will be sent information.
- 'Enrol Now' button
Nice to have
• - Simple list of courses that we offer

```html
<!DOCTYPE html>
<html lang="en">
<head>
<meta charset="utf-8">
<title>Fernbrook Institute – Accounting training for the real world</title>
<link href="https://fonts.googleapis.com/css2?family=Poppins:wght@400;500;600&display=swap" rel="stylesheet">
<style>
:root{
  --blue:#3276b5;
  --blue-soft:#85acd3;
  --navy:#1c2b4a;
  --footer:#1f2d50;
  --ink:#1e1e1e;
  --line:#e2e4e8;
  --grey-bg:#f5f6f7;
  --field:#f4f5f6;
  --white:#fff;
}
*{box-sizing:border-box;margin:0;padding:0}
html,body{width:1200px;height:3463px;overflow:hidden}
body{font-family:'Poppins',sans-serif;color:var(--ink);background:var(--white);position:relative}
a{color:inherit;text-decoration:none}
.btn-outline{position:absolute;border:1px solid #c9ccd2;background:#fff;font-size:13px;color:#333;display:flex;align-items:center;justify-content:center}
.btn-solid{position:absolute;background:var(--blue);color:#fff;font-size:13px;display:flex;align-items:center;justify-content:center}
.section-title{position:absolute;left:0;width:1200px;text-align:center;color:var(--blue);font-weight:500;font-size:25px}

/* header */
.site-header{position:absolute;left:0;top:0;width:1200px;height:78px;background:#fff}
.logo{position:absolute;left:126px;top:0;width:102px;height:102px;background:var(--navy);color:#fff;display:flex;flex-direction:column;align-items:center;justify-content:flex-end;padding-bottom:14px;z-index:3}
.logo-mark{width:20px;height:20px;background:#fff;margin-bottom:10px}
.logo-name{font-size:13px;font-weight:500;letter-spacing:.5px}
.logo-sub{font-size:8px;letter-spacing:1px}
.main-nav{position:absolute;left:342px;top:32px;display:flex;gap:27px;font-size:14px;font-weight:500}
.main-nav .active{color:var(--blue);border-bottom:1px solid var(--blue)}
.call{position:absolute;left:806px;top:26px;display:flex;align-items:center;gap:10px}
.call small{display:block;font-size:9px;color:#444}
.call strong{font-size:15px;font-weight:600}
.search-btn{position:absolute;left:957px;top:24px;width:32px;height:30px;background:var(--navy)}
.login-btn{position:absolute;left:998px;top:24px;width:76px;height:30px;background:var(--blue);color:#fff;font-size:13px;display:flex;align-items:center;justify-content:center}

/* hero */
.hero{position:absolute;left:0;top:78px;width:1200px;height:520px;background:linear-gradient(100deg,#f1f1ef 0%,#e4e2dd 40%,#c9c4bb 70%,#e8e6e2 100%)}
.hero h1{position:absolute;left:174px;top:190px;font-size:33px;line-height:41px;font-weight:600;color:var(--navy)}
.hero .enrol{position:absolute;left:174px;top:284px;font-size:18px;font-weight:500;color:var(--blue);border-bottom:2px solid var(--blue)}
.form-band{position:absolute;left:744px;top:598px;width:354px;height:188px;background:var(--blue)}
.lead-form{position:absolute;left:767px;top:239px;width:307px;height:524px;background:#fff;box-shadow:0 2px 10px rgba(0,0,0,.08);padding:22px 12px 0}
.lead-form h2{text-align:center;color:var(--blue);font-size:20px;line-height:24px;font-weight:600}
.lead-form p{text-align:center;font-size:11.5px;line-height:15px;color:#333;margin:12px 8px 18px}
.field{height:36px;background:var(--field);margin:0 0 10px 0;width:283px;font-size:11px;color:#888;display:flex;align-items:center;justify-content:space-between;padding:0 12px}
.field .caret{width:0;height:0;border-left:4px solid transparent;border-right:4px solid transparent;border-top:4px solid #888}
.tick{font-size:12px;text-align:center;margin:14px 0 16px;display:flex;justify-content:center;align-items:center;gap:8px}
.tick span{width:16px;height:16px;border:1px solid #ccc;display:inline-block}
.submit{width:283px;height:36px;background:var(--blue);color:#fff;font-size:13px;font-weight:500;display:flex;align-items:center;justify-content:center}

.strip{position:absolute;left:126px;top:598px;width:618px;height:188px;border:1px solid var(--line);border-top:none}
.strip-divider{position:absolute;left:308px;top:0;width:1px;height:188px;background:var(--line)}
.strip h3{position:absolute;left:26px;top:52px;font-size:21px;line-height:25px;font-weight:400}
.strip .btn-outline{left:28px;top:122px;width:126px;height:34px}
.review-name{position:absolute;left:308px;width:310px;top:50px;display:flex;align-items:center;justify-content:center;gap:8px;font-size:22px;font-weight:500}
.review-name i{width:20px;height:20px;background:var(--blue);display:inline-block}
.rating{position:absolute;left:308px;width:310px;top:92px;display:flex;justify-content:center;gap:4px}
.review-score{position:absolute;left:308px;width:310px;top:130px;text-align:center;font-size:13px}

/* why */
.why-photo{position:absolute;left:126px;top:825px;width:250px;height:137px;background:linear-gradient(135deg,#8a8f96,#c3c7cc 50%,#5e6a79)}
.why h2{position:absolute;left:409px;top:820px;font-size:24px;font-weight:500;color:var(--blue)}
.why p{position:absolute;left:409px;top:862px;width:665px;font-size:14px;line-height:21px;color:#333}
.why .btn-outline{left:409px;top:922px;width:100px;height:28px;font-size:12px}

/* courses */
.learn{position:absolute;left:0;top:1001px;width:1200px;height:538px;background:var(--grey-bg)}
.course{position:absolute;width:176px;height:176px;background:#fff;border:1px solid var(--line);display:flex;flex-direction:column;align-items:center;justify-content:flex-end;padding-bottom:18px;text-align:center;font-size:15px;line-height:19px}
.course svg{position:absolute;top:38px;left:58px}
.course.featured{background:var(--blue-soft);color:#fff;border-color:var(--blue-soft)}

/* video */
.video{position:absolute;left:0;top:1539px;width:611px;height:477px;background:linear-gradient(120deg,#6c6a66,#b5aea4 45%,#8b7c6c)}
.play{position:absolute;left:250px;top:1726px;width:100px;height:100px;border-radius:50%;background:rgba(255,255,255,.75);display:flex;align-items:center;justify-content:center}
.play i{display:block;width:70px;height:70px;border-radius:50%;background:#fff;position:relative}
.play i::after{content:"";position:absolute;left:28px;top:20px;border-left:24px solid var(--blue);border-top:15px solid transparent;border-bottom:15px solid transparent}
.different h2{position:absolute;left:611px;width:589px;top:1590px;text-align:center;font-size:24px;line-height:26px;font-weight:600;color:var(--blue)}
.perk{position:absolute;left:679px;width:358px;height:84px;background:#fff;box-shadow:0 2px 12px rgba(0,0,0,.08);display:flex;align-items:center;font-size:15px;line-height:22px}
.perk svg{margin:0 24px;flex:none}

/* rank */
.rank{position:absolute;left:0;top:2016px;width:1200px;height:309px;background:var(--blue);color:#fff}
.rank h2{position:absolute;left:0;width:1200px;top:50px;text-align:center;font-size:25px;font-weight:500}
.rank p{position:absolute;left:250px;width:700px;top:94px;text-align:center;font-size:13px;line-height:21px;color:#dce8f4}
.stat{position:absolute;top:160px;width:274px;height:80px;border:1px solid rgba(255,255,255,.35);display:flex;align-items:center}
.stat::after{content:"";position:absolute;left:0;bottom:0;width:244px;height:4px;background:var(--navy)}
.stat b{font-size:23px;font-weight:600;margin:0 22px 0 30px}
.stat span{font-size:16px;line-height:22px}

/* blogs */
.view-all{position:absolute;left:1017px;top:2389px;font-size:13px;color:#333;border-bottom:1px solid #333}
.blog-photo{position:absolute;top:2438px;width:300px;height:181px}
.blog-title{position:absolute;top:2641px;width:290px;font-size:14.5px;line-height:21px}
.blog-date{position:absolute;top:2699px;font-size:11.5px;display:flex;align-items:center;gap:8px}
.blog .btn-outline,.blog .btn-solid{top:2694px;width:100px;height:28px;font-size:12px}

/* accredit */
.accredit{position:absolute;left:0;top:2775px;width:1200px;height:285px;background:var(--grey-bg)}
.badge{position:absolute;top:2876px;width:176px;height:81px;background:#fff;display:flex;align-items:center;justify-content:center}
.badge i{display:block;width:110px;height:34px;background:#d9dce1;border-radius:4px}
.arrow-left{position:absolute;left:563px;top:2998px}
.arrow-right{position:absolute;left:602px;top:2988px;width:42px;height:24px;background:var(--blue);display:flex;align-items:center;justify-content:center}

/* footer */
.site-footer{position:absolute;left:0;top:3060px;width:1200px;height:360px;background:var(--footer);color:#fff}
.fcol{position:absolute;top:38px}
.fcol h4{font-size:17px;font-weight:500;color:var(--blue)}
.fcol h4::after{content:"";display:block;width:30px;height:2px;background:var(--blue);margin:8px 0 12px}
.fcol li{list-style:none;font-size:12.5px;line-height:22px}
.fcol li.current{color:var(--blue)}
.city{width:158px;height:35px;border:1px solid rgba(255,255,255,.3);font-size:13px;display:flex;align-items:center;justify-content:center;margin-bottom:10px}
.socials{display:flex;gap:12px}
.socials span{width:25px;height:25px;border:1px solid #fff;border-radius:50%;display:block}
.foot-phone{position:absolute;left:520px;top:325px;font-size:16px;color:var(--blue);display:flex;gap:12px;align-items:center}
.copyright{position:absolute;left:0;top:3420px;width:1200px;height:43px;background:var(--blue);color:#fff;font-size:13px;display:flex;align-items:center;justify-content:center}
</style>
</head>
<body>

<header class="site-header">
  <div class="logo"><span class="logo-mark"></span><span class="logo-name">FERNBROOK</span><span class="logo-sub">INSTITUTE</span></div>
  <nav class="main-nav">
    <a class="active">Home</a><a>Courses</a><a>About</a><a>More info</a><a>Blogs</a><a>Contact</a>
  </nav>
  <div class="call">
    <svg width="20" height="20" viewBox="0 0 24 24"><path fill="#3276b5" d="M6.6 10.8a15 15 0 0 0 6.6 6.6l2.2-2.2c.3-.3.7-.4 1-.2 1.1.4 2.3.6 3.6.6.6 0 1 .4 1 1V20c0 .6-.4 1-1 1A17 17 0 0 1 3 4c0-.6.4-1 1-1h3.5c.6 0 1 .4 1 1 0 1.3.2 2.5.6 3.6.1.3 0 .7-.2 1z"/></svg>
    <div><small>Call No.:</small><strong>1300 555 019</strong></div>
  </div>
  <div class="search-btn"><svg width="32" height="30" viewBox="0 0 32 30"><circle cx="15" cy="14" r="5" fill="none" stroke="#fff" stroke-width="2"/><path d="M19 18l4 4" stroke="#fff" stroke-width="2"/></svg></div>
  <a class="login-btn">➜&nbsp; Login</a>
</header>

<section class="hero">
  <div role="img" aria-label="Smiling student in glasses studying at a laptop" style="position:absolute;inset:0"></div>
  <h1>Accounting training.<br>For the real world.</h1>
  <a class="enrol">Enrol Now</a>
</section>

<div class="form-band"></div>
<form class="lead-form">
  <h2>Any questions?<br>Ask away!</h2>
  <p>Please complete the details below. Your dedicated course consultant will be in touch with you shortly.</p>
  <div class="field">Full Name</div>
  <div class="field">Email</div>
  <div class="field">Phone</div>
  <div class="field">State<span class="caret"></span></div>
  <div class="field">Course<span class="caret"></span></div>
  <div class="field">Message</div>
  <div class="tick">Tick if you prefer we email you <span></span></div>
  <div class="submit">SUBMIT</div>
</form>

<div class="strip">
  <h3>It’s education.<br>But not as you know it.</h3>
  <a class="btn-outline">Learn More</a>
  <div class="strip-divider"></div>
  <div class="review-name"><i></i>Reviewly</div>
  <div class="rating" aria-label="Rated 4.7 out of 5">
    <svg width="22" height="22" viewBox="0 0 24 24"><path fill="#3276b5" d="M12 2l3 7h7l-5.5 4.5 2 7.5-6.5-4.5L5.5 21l2-7.5L2 9h7z"/></svg>
    <svg width="22" height="22" viewBox="0 0 24 24"><path fill="#3276b5" d="M12 2l3 7h7l-5.5 4.5 2 7.5-6.5-4.5L5.5 21l2-7.5L2 9h7z"/></svg>
    <svg width="22" height="22" viewBox="0 0 24 24"><path fill="#3276b5" d="M12 2l3 7h7l-5.5 4.5 2 7.5-6.5-4.5L5.5 21l2-7.5L2 9h7z"/></svg>
    <svg width="22" height="22" viewBox="0 0 24 24"><path fill="#3276b5" d="M12 2l3 7h7l-5.5 4.5 2 7.5-6.5-4.5L5.5 21l2-7.5L2 9h7z"/></svg>
    <svg width="22" height="22" viewBox="0 0 24 24"><path fill="#3276b5" d="M12 2l3 7h7l-5.5 4.5 2 7.5-6.5-4.5L5.5 21l2-7.5L2 9h7z"/></svg>
  </div>
  <div class="review-score">Rating 4.7 &nbsp;&nbsp;|&nbsp;&nbsp; 554 reviews</div>
</div>

<section class="why">
  <div class="why-photo" role="img" aria-label="Student working in a bright open-plan study space"></div>
  <h2>Why Fernbrook is your Best Educator Partner</h2>
  <p>You deserve a learning experience that leaves you ready for the real world. Not just for the classroom. That’s why Fernbrook Institute delivers real-world education. We start with...</p>
  <a class="btn-outline">Read More</a>
</section>

<section class="learn"></section>
<h2 class="section-title" style="top:1050px">What will you learn next?</h2>

<div class="course" style="left:126px;top:1114px"><svg width="60" height="56" viewBox="0 0 60 56" fill="none" stroke="#3276b5" stroke-width="1.6"><rect x="8" y="6" width="44" height="44" rx="3"/><rect x="22" y="12" width="24" height="10"/><path d="M22 28h6v6h-6zM32 28h6v6h-6zM42 28h4v6h-4zM22 38h6v6h-6zM32 38h6v6h-6z"/></svg>Accounting &amp;<br>Bookkeeping</div>
<div class="course" style="left:318px;top:1114px"><svg width="60" height="56" viewBox="0 0 60 56" fill="none" stroke="#3276b5" stroke-width="1.6"><rect x="14" y="6" width="32" height="44" rx="2"/><path d="M22 18h16M22 26h16M22 34h16M24 42h12"/></svg>Financial<br>Planning</div>
<div class="course featured" style="left:512px;top:1114px"><svg width="60" height="56" viewBox="0 0 60 56" fill="none" stroke="#fff" stroke-width="1.6"><circle cx="30" cy="28" r="12"/><circle cx="30" cy="28" r="5"/><circle cx="30" cy="6" r="3"/><circle cx="30" cy="50" r="3"/><circle cx="8" cy="28" r="3"/><circle cx="52" cy="28" r="3"/></svg>Business &amp;<br>Management</div>
<div class="course" style="left:704px;top:1114px"><svg width="60" height="56" viewBox="0 0 60 56" fill="none" stroke="#3276b5" stroke-width="1.6"><path d="M6 50h48M10 50V30h40v20M16 30v20M22 30v20M28 30v20M34 30v20M40 30v20M30 8v22M22 22l8-6 8 6"/></svg>Transport &amp;<br>Logistics</div>
<div class="course" style="left:896px;top:1114px"><svg width="60" height="56" viewBox="0 0 60 56" fill="none" stroke="#3276b5" stroke-width="1.6"><rect x="26" y="6" width="22" height="36" rx="2"/><path d="M10 28h14v20H10zM30 14h14M30 22h14"/></svg>Finance &amp; Mort-<br>gage Broking</div>

<div class="course" style="left:126px;top:1306px"><svg width="60" height="56" viewBox="0 0 60 56" fill="none" stroke="#3276b5" stroke-width="1.6"><path d="M6 50h48M10 50V30h40v20M8 30h44l-22-12zM16 34v12M24 34v12M36 34v12M44 34v12M30 18V6h8v4h-8"/></svg>Governance</div>
<div class="course" style="left:318px;top:1306px"><svg width="60" height="56" viewBox="0 0 60 56" fill="none" stroke="#3276b5" stroke-width="1.6"><circle cx="34" cy="22" r="12"/><circle cx="34" cy="22" r="5"/><path d="M14 50V34c0-6 6-10 10-10"/></svg>Project<br>Management</div>
<div class="course" style="left:512px;top:1306px"><svg width="60" height="56" viewBox="0 0 60 56" fill="none" stroke="#3276b5" stroke-width="1.6"><path d="M12 30l26-16v32L12 34zM12 30v4M18 35l4 12h6l-3-10M44 20l6-4M46 30h6M44 40l6 4"/></svg>Marketing</div>
<div class="course" style="left:704px;top:1306px"><svg width="60" height="56" viewBox="0 0 60 56" fill="none" stroke="#3276b5" stroke-width="1.6"><circle cx="30" cy="22" r="18"/><circle cx="30" cy="18" r="6"/><path d="M20 34c2-6 18-6 20 0M30 40v14"/></svg>Human Resources</div>

<section class="different">
  <div class="video" role="img" aria-label="Video: student celebrating success at her desk"></div>
  <a class="play" href="https://vidhost.example/qT7mWx2LcaB" aria-label="Play video"><i></i></a>
  <h2>We’re a little different.<br>With us you’ll get...</h2>
  <div class="perk" style="top:1668px"><svg width="44" height="50" viewBox="0 0 44 50" fill="none" stroke="#222" stroke-width="1.4"><circle cx="22" cy="18" r="14"/><circle cx="22" cy="18" r="8"/><path d="M14 30l-6 16 6-3 3 5 5-14M30 30l6 16-6-3-3 5-5-14"/></svg>Get the skills that<br>employers really want.</div>
  <div class="perk" style="top:1769px"><svg width="62" height="40" viewBox="0 0 62 40" fill="none" stroke="#222" stroke-width="1.4"><rect x="10" y="4" width="42" height="18" rx="3"/><rect x="2" y="16" width="10" height="16" rx="3"/><rect x="50" y="16" width="10" height="16" rx="3"/><path d="M12 26h38M8 32v6M54 32v6"/></svg>Absolute flexibility.<br>Your way, your terms.</div>
  <div class="perk" style="top:1868px"><svg width="52" height="52" viewBox="0 0 52 52" fill="none" stroke="#222" stroke-width="1.4"><circle cx="26" cy="26" r="22"/><circle cx="26" cy="26" r="18"/><path d="M26 12v14l10 8"/></svg>Unrivalled support.<br>Delivered with care.</div>
</section>

<section class="rank">
  <h2>How we rank</h2>
  <p>Every month we measure our student’s feedback. This keeps us on our toes, so our courses and support stay ahead of the pack. Here’s what they have to say this month...</p>
  <div class="stat" style="left:165px"><b>91%</b><span>Would recommend<br>to a friend</span></div>
  <div class="stat" style="left:463px"><b>94%</b><span>Are satisfied<br>with the training</span></div>
  <div class="stat" style="left:760px"><b>89%</b><span>Are happy with our<br>responsiveness</span></div>
</section>

<section class="blog">
  <h2 class="section-title" style="top:2374px">Blogs</h2>
  <a class="view-all">View All</a>
  <div class="blog-photo" style="left:126px;background:linear-gradient(135deg,#d8d5d0,#a9a39b 60%,#e07a5f)" role="img" aria-label="Bookkeeper at her office desk"></div>
  <div class="blog-photo" style="left:450px;background:linear-gradient(135deg,#eef0f2,#8d939c 55%,#3d4a63)" role="img" aria-label="Two colleagues reviewing a tablet"></div>
  <div class="blog-photo" style="left:774px;background:linear-gradient(135deg,#2e3440,#5b6574 55%,#9aa3ad)" role="img" aria-label="Student studying online on a laptop"></div>
  <div class="blog-title" style="left:126px">How to become a certified bookkeeper<br>in Australia</div>
  <div class="blog-title" style="left:450px">What’s the difference between para-<br>planning and financial planning?</div>
  <div class="blog-title" style="left:774px">Top 20 free online courses you can<br>start today</div>
  <div class="blog-date" style="left:126px"><svg width="14" height="14" viewBox="0 0 14 14" fill="none" stroke="#3276b5" stroke-width="1.4"><rect x="1" y="2" width="12" height="11"/><path d="M1 6h12M4 0v3M10 0v3"/></svg>30 Nov, 2020</div>
  <div class="blog-date" style="left:450px"><svg width="14" height="14" viewBox="0 0 14 14" fill="none" stroke="#3276b5" stroke-width="1.4"><rect x="1" y="2" width="12" height="11"/><path d="M1 6h12M4 0v3M10 0v3"/></svg>30 Nov, 2020</div>
  <div class="blog-date" style="left:774px"><svg width="14" height="14" viewBox="0 0 14 14" fill="none" stroke="#3276b5" stroke-width="1.4"><rect x="1" y="2" width="12" height="11"/><path d="M1 6h12M4 0v3M10 0v3"/></svg>30 Nov, 2020</div>
  <a class="btn-solid" style="left:239px">Read More</a>
  <a class="btn-outline" style="left:563px">Read More</a>
  <a class="btn-outline" style="left:887px">Read More</a>
</section>

<section class="accredit"></section>
<h2 class="section-title" style="top:2820px">We’re nationally accredited. And industry accredited...</h2>
<div class="badge" style="left:126px"><i></i></div>
<div class="badge" style="left:318px"><i></i></div>
<div class="badge" style="left:512px"><i></i></div>
<div class="badge" style="left:704px"><i></i></div>
<div class="badge" style="left:896px"><i></i></div>
<svg class="arrow-left" width="22" height="8" viewBox="0 0 22 8"><path d="M22 4H2M5 1L1 4l4 3" fill="none" stroke="#333" stroke-width="1.4"/></svg>
<div class="arrow-right"><svg width="22" height="8" viewBox="0 0 22 8"><path d="M0 4h20M17 1l4 3-4 3" fill="none" stroke="#fff" stroke-width="1.4"/></svg></div>

<footer class="site-footer">
  <div class="fcol" style="left:126px"><h4>Courses</h4><ul>
    <li class="current">Overview</li><li>Accounting and Bookkeeping</li><li>Business and Management</li><li>Financial Planning and Paraplanning</li><li>Finance and Mortgage Broking</li><li>Governance</li><li>Human Resources</li><li>Marketing</li><li>Project Management</li><li>RG146 Training Courses</li><li>Transport and Logistics</li><li>Short Courses</li></ul></div>
  <div class="fcol" style="left:408px"><h4>More Info</h4><ul>
    <li>Enrol Now</li><li>Student Info</li><li>Government funding</li><li>Studying online</li><li>Videos</li><li>Blog</li><li>Frequently Asked Questions</li></ul></div>
  <div class="fcol" style="left:678px"><h4>About</h4><ul>
    <li>Overview</li><li>Student Reviews</li><li>Board of Directors</li><li>Trainers</li></ul>
    <h4 style="margin-top:30px">Followers Us</h4>
    <div class="socials"><span></span><span></span><span></span></div></div>
  <div class="fcol" style="left:915px"><h4>Conatct info</h4>
    <div class="city">Melbourne</div><div class="city">Sydney</div><div class="city">Brisbane</div><div class="city">Perth</div></div>
  <div class="foot-phone"><svg width="18" height="18" viewBox="0 0 24 24"><path fill="#3276b5" d="M6.6 10.8a15 15 0 0 0 6.6 6.6l2.2-2.2c.3-.3.7-.4 1-.2 1.1.4 2.3.6 3.6.6.6 0 1 .4 1 1V20c0 .6-.4 1-1 1A17 17 0 0 1 3 4c0-.6.4-1 1-1h3.5c.6 0 1 .4 1 1 0 1.3.2 2.5.6 3.6.1.3 0 .7-.2 1z"/></svg>1300 555 019 (local) , +(613) 9000 0142 (international)</div>
</footer>
<div class="copyright">Copyright © 2020 Fernbrook. All Rights Reserved</div>

</body>
</html>
```